heron works we are a building company, commercial/retail/residential

will like a company car wrap design. ill be getting have wrap van, full wrap utes.
we specialize in high end residential homes, and shop fit outs. our company is based in Sydney and will like to show company website (heronworksbuild.com.au) also Instagram (heron_works)
A design for our company cars that looks elegant.

```html
<!DOCTYPE html>
<html lang="en">
<head>
<meta charset="utf-8">
<title>Heron Works – Van Wrap</title>
<link rel="stylesheet" href="https://fonts.googleapis.com/css2?family=Poppins:ital,wght@0,400;0,500;0,600;1,600&display=swap">
<style>
  :root {
    --backdrop: #a7a7a7;
    --body-white: #f4f5f7;
    --body-shade: #dfe1e5;
    --brand-blue: #21417f;
    --brand-blue-light: #2d5096;
    --ink-navy: #14244a;
    --glass: #4c4f55;
    --glass-light: #8b8e93;
    --trim: #1c1d20;
    --tyre: #1b1b1c;
    --rim: #c9cbcf;
    --tail-red: #c4161c;
    --text-white: #ffffff;
  }
  html, body {
    margin: 0;
    padding: 0;
    width: 1200px;
    height: 800px;
    overflow: hidden;
    background: var(--backdrop);
  }
  .canvas {
    position: relative;
    width: 1200px;
    height: 800px;
    font-family: "Poppins", sans-serif;
  }
  .van-side {
    position: absolute;
    inset: 0;
  }
  .brand-name {
    font-family: "Poppins", sans-serif;
    font-weight: 600;
    font-size: 34px;
    fill: var(--text-white);
  }
  .tagline {
    font-family: "Poppins", sans-serif;
    font-size: 20px;
    fill: var(--text-white);
  }
  .tagline-strong {
    font-weight: 600;
    font-style: italic;
  }
  .phone-number {
    font-family: "Poppins", sans-serif;
    font-weight: 500;
    font-size: 14px;
    fill: var(--text-white);
  }
  .contact-line {
    font-family: "Poppins", sans-serif;
    font-weight: 500;
    font-size: 11.5px;
    fill: var(--ink-navy);
  }
</style>
</head>
<body>
<main class="canvas">
  <svg class="van-side" viewBox="0 0 1200 800" width="1200" height="800" aria-label="Heron Works van wrap, side view">
    <defs>
      <clipPath id="body-clip">
        <path d="M220,520 L220,425 Q222,410 240,404 L340,372 Q400,320 470,280 Q520,266 580,264 L930,264 Q944,266 948,290 L978,420 Q986,450 986,480 L986,500 Q984,505 960,505 L220,520 Z"/>
      </clipPath>
    </defs>

    <ellipse class="ground-shadow" cx="600" cy="540" rx="430" ry="8" fill="#000" opacity="0.25"/>

    <path class="body-panel" d="M220,520 L220,425 Q222,410 240,404 L340,372 Q400,320 470,280 Q520,266 580,264 L930,264 Q944,266 948,290 L978,420 Q986,450 986,480 L986,500 Q984,505 960,505 L220,520 Z" fill="var(--body-white)"/>

    <g clip-path="url(#body-clip)">
      <path class="wrap-sweep" d="M658,262 H934 Q946,330 944,420 Q942,452 924,460 L904,470 L900,520 H400 V494 Q590,492 636,400 Q660,340 658,262 Z" fill="var(--brand-blue)"/>
      <path class="wrap-highlight" d="M658,262 H934 Q940,300 942,350 L650,368 Q660,320 658,262 Z" fill="var(--brand-blue-light)" opacity="0.55"/>
      <rect class="sill-shade" x="220" y="503" width="770" height="20" fill="#000" opacity="0.08"/>
    </g>

    <rect class="cargo-recess" x="590" y="278" width="66" height="86" rx="4" fill="none" stroke="var(--body-shade)" stroke-width="1.5"/>

    <path class="door-seam" d="M412,326 L414,506 M578,272 L579,502" stroke="#b9bcc2" stroke-width="1.2" fill="none"/>

    <path class="front-quarter-glass" d="M372,378 L410,345 L410,372 Z" fill="var(--glass)"/>
    <path class="door-glass" d="M420,336 Q470,300 556,282 L558,372 L420,378 Z" fill="var(--glass)" stroke="var(--trim)" stroke-width="2"/>
    <path class="door-glass-sheen" d="M440,340 Q490,310 548,296 L550,366 L470,370 Z" fill="var(--glass-light)" opacity="0.35"/>
    <rect class="mirror" x="417" y="355" width="28" height="22" rx="5" fill="var(--trim)"/>
    <rect class="door-handle" x="523" y="380" width="40" height="8" rx="4" fill="#9a9da3"/>

    <path class="head-lamp" d="M228,428 L292,398 Q280,415 240,440 Z" fill="#6a6d72"/>
    <rect class="tail-lamp" x="966" y="366" width="14" height="58" rx="3" fill="var(--tail-red)"/>

    <path class="front-arch" d="M278,510 A60,60 0 0 1 396,510 Z" fill="var(--trim)"/>
    <path class="rear-arch" d="M778,508 A60,60 0 0 1 896,508 Z" fill="var(--trim)"/>

    <g class="wheel front-wheel">
      <circle cx="337" cy="497" r="52" fill="var(--tyre)"/>
      <circle cx="337" cy="497" r="38" fill="var(--rim)"/>
      <circle cx="337" cy="497" r="15" fill="#2a2b2d"/>
    </g>
    <g class="wheel rear-wheel">
      <circle cx="837" cy="497" r="52" fill="var(--tyre)"/>
      <circle cx="837" cy="497" r="38" fill="var(--rim)"/>
      <circle cx="837" cy="497" r="15" fill="#2a2b2d"/>
    </g>

    <g class="brand-lockup">
      <rect class="brand-square" x="672" y="305" width="22" height="22" fill="var(--text-white)"/>
      <text class="brand-name" x="704" y="328" textLength="212" lengthAdjust="spacingAndGlyphs">Heron Works</text>
    </g>

    <text class="tagline" x="672" y="416" textLength="240" lengthAdjust="spacingAndGlyphs">You dream it, <tspan class="tagline-strong">We build it.</tspan></text>

    <g class="contact-block">
      <rect class="phone-pill" x="418" y="422" width="124" height="18" rx="9" fill="var(--brand-blue)"/>
      <circle class="phone-icon-ring" cx="427" cy="431" r="7" fill="none" stroke="#fff" stroke-width="1.4"/>
      <path class="phone-icon" d="M424,427.5 q0.8,-0.8 1.6,0 l0.8,1.2 q0.3,0.6 -0.3,1 q0.6,1.5 1.9,2.3 q0.5,-0.6 1,-0.3 l1.2,0.8 q0.7,0.7 0,1.5 q-1.4,1 -3.6,-0.8 q-2.2,-2 -2.6,-4 z" fill="#fff"/>
      <text class="phone-number" x="437" y="436">0400 318 726</text>

      <circle class="web-icon" cx="427" cy="449" r="5.5" fill="var(--brand-blue)"/>
      <text class="contact-line" x="437" y="453">heronworksbuild.com.au</text>

      <circle class="social-icon" cx="427" cy="466" r="5.5" fill="var(--brand-blue)"/>
      <text class="contact-line" x="437" y="470">heron_works</text>
    </g>
  </svg>
</main>
</body>
</html>
```